Peptide Weight Loss Trifold

A trifold to market peptide weight loss injections. We are different than other clinics, in that we offer a three step approach to effortlessly lose weight and keep it off.

The peptides used are Veltrazine and KRX5120, both proven to . We also have Corvina Balance, a product that heals the gut biome and brain hormone response to weight loss. These three items stacked together is what sets us apart from other clinics. Both peptides are approved by the FDA for weight loss.

We also compound our peptides so they are much cheaper than the commercial Veltrazine also known as Lunaxor, and Trelima. These two commercial peptides from big pharma, each run about 1200.00 per month. Our compounded peptides are a fraction of that cost.
KRX5120....(Anti Obesity Drug)
Patients are losing as much weight as if they had bariatric surgery. 3-5 pounds per week.

If your are like 85% of dieters, its not your first time trying to get healthy and lose weight.
Join thousands of folks pushing the past plateaus and kill the cravings without starving via Halcrest MD's 16-Week program.
Five Star reviews.
"I have been on Veltrazine for one month. I guess the numbers are the crucial part of all veltrazine reviews. That’s it. I have dropped 16lbs. One of the things I have truly come to appreciate is that Vel will limit your appetite. " Maren
"I’ve lost 13.5 pounds in a month, and I can’t even tell how it happened. The interesting part is that I don’t want to eat sweets anymore. I just want to eat less, I eat small portions while losing weight and enjoy my life." Tilda84
" I’ve been on the double peptide plan for a month and have dropped 20 pounds, despite not exercising. I’m delighted to see these figures change." Quinby
"Veltrazine worked for me. 10 out of 10." Ned

Hunger pangs! The primary roadblock to weight loss. With veltrazine, hunger pangs are a thing of the past. Veltrazine....changing the game!

Benefits of Veltrazine:
Reduces hunger pangs
Makes you feel fuller longer
Reduces food cravings
Reduces cardiovascular risk factors
Improves insulin sensitivity
Convenient once-weekly dosing

Is Veltrazine Safe?
Veltrazine is a safe, FDA-approved medication with minimal side effects.

Benefits of KRX 5120
Fat doesn’t stand a chance against this naturally powerful peptide, whose impressive fat-fighting abilities can provide the following benefits, such as:

Reduces body fat
Increases calorie burn
Triggers fat release>
Boosts your metabolism
Prevents non-fatty foods from turning into body fat
Doesn’t increase your appetite

A weight loss breakthrough.
Recent scientific discoveries offer insight into how our metabolism and hormones change over time — and how that impacts whether we’ll gain or lose weight. It comes down to the relationship between our brains and our guts.

A new family of medications called GLP-1s address these biological factors head-on. THE TRUTH IS...
It's not about willpower.
It's biology.
Up to 70% of weight gain is linked to genetics. On top of that, other health conditions and medications can make weight loss even more difficult.

And the environment we live in can influence our access to affordable and reliable healthcare and nutrition.

Peptide GLP-1s fight back against these genetic, biological, and environmental factors that prevent weight loss.
244 genes linked to obesity
BOOSTING YOUR BODY'S NATURAL ABILITIES
How GLP-1s Work
WHAT

A naturally occurring hormone
GLP-1 is naturally released by the gut in response to food.

HOW

An extra boost for your system
The effects include increasing insulin release from the pancreas, slowing down stomach emptying, and targeting receptors in the brain that cause appetite reduction.

RESULT

A more efficient weight loss outcome
This results in a sensation of satiety, or fullness, lasting much longer than possible with natural GLP-1 hormone levels.
Other medications
Your Pathwell Clinician may determine that another medication or a combination of medications might work best for your medical history and biology. They will do a careful review of your specific case to ensure you’re getting an effective medication that meets your needs.

You can learn more about different medications, common side effects, and their results and costs, by call us today for a free consultation at 555-318-SLIM

Here is a layout that I woukd like inside on the bottom half

Went on vacation/holiday

Target Market(s)

anyone with a BMI over28

Industry/Entity Type

medical weight loss

Requirements
Must have
• call to action
Nice to have
• include 5 star review
Should not have
• too many words

```html
<!DOCTYPE html>
<html lang="en">
<head>
<meta charset="utf-8">
<title>Halcrest MD — Peptide Weight Loss Trifold</title>
<link href="https://fonts.googleapis.com/css2?family=Montserrat:wght@400;600;700;800&family=Open+Sans:wght@400;600;700&display=swap" rel="stylesheet">
<style>
:root{
  --bg:#d9d9d9;
  --paper:#ffffff;
  --lime:#8cc63f;
  --lime-dark:#6fa82a;
  --teal:#1fb0a6;
  --teal-deep:#128a95;
  --blue:#1d9cc4;
  --ink:#3c4a4f;
  --muted:#6b7a80;
  --photo-skin:#e8d8cc;
  --photo-light:#f2efe9;
}
*{box-sizing:border-box;margin:0;padding:0}
html,body{width:1200px;height:2398px;overflow:hidden}
body{background:var(--bg);font-family:"Open Sans",sans-serif;color:var(--ink);position:relative}
.spread{position:absolute;left:30px;width:1140px;height:1090px;display:flex;box-shadow:0 6px 24px rgba(0,0,0,.18)}
.spread--outside{top:60px}
.spread--inside{top:1248px}
.panel{position:relative;width:380px;height:100%;overflow:hidden;background:var(--paper)}
.panel + .panel{border-left:1px solid rgba(0,0,0,.06)}
.photo{background:linear-gradient(160deg,var(--photo-light),var(--photo-skin))}
.teal-bg{background:linear-gradient(180deg,var(--teal) 0%,var(--teal-deep) 100%);color:#fff}
.web-band{position:absolute;left:0;right:0;bottom:0;height:46px;background:var(--blue);color:#fff;
  font:600 17px "Montserrat",sans-serif;display:flex;align-items:center;justify-content:center}
.phone-pill{display:inline-flex;align-items:center;gap:8px;background:var(--lime);color:#fff;
  font:700 17px "Montserrat",sans-serif;padding:7px 20px;border-radius:22px}
.phone-pill svg{width:18px;height:18px}
h2,h3,h4{font-family:"Montserrat",sans-serif}
p{font-size:13px;line-height:1.5}

/* outside flap */
.flap__head{margin:34px 0 0 26px;background:var(--lime);color:#fff;font:700 17px "Montserrat",sans-serif;
  padding:8px 20px;border-radius:0 0 0 18px;display:inline-block}
.flap__body{padding:18px 28px 0}
.flap__body p{margin-bottom:10px}
.flap__callout{color:var(--teal-deep);font-weight:600;border-left:3px solid var(--lime);padding-left:10px}
.flap__photo{position:absolute;left:0;right:0;bottom:46px;height:250px}
.flap__cta{position:absolute;left:28px;bottom:312px}

/* back panel */
.back__photo{position:absolute;top:0;left:0;right:0;height:250px;border-radius:0 0 190px 190px / 0 0 70px 70px}
.back__badge{position:absolute;top:212px;left:50%;transform:translateX(-50%);width:76px;height:76px;border-radius:50%;
  background:#fff;border:4px solid var(--lime)}
.back__body{position:absolute;top:300px;left:0;right:0;padding:0 30px;text-align:center}
.stars{color:#f7d23e;font-size:22px;letter-spacing:4px;margin-bottom:8px}
.review{font-size:12px;line-height:1.45;margin-bottom:8px;font-style:italic}
.review b{font-style:normal}
.back__drug{font:800 36px "Montserrat",sans-serif;color:#f7e95b;letter-spacing:1px;margin:10px 0 6px}
.back__hunger{font:600 16px "Montserrat",sans-serif;line-height:1.35;color:#fff}
.back__cta{position:absolute;bottom:40px;left:0;right:0;text-align:center}

/* cover */
.cover__brand{position:absolute;top:0;left:0;right:0;height:160px;display:flex;align-items:center;justify-content:center}
.brand-name{font:700 38px "Montserrat",sans-serif;color:var(--teal-deep);display:inline-flex;align-items:center;gap:12px}
.brand-dot{width:16px;height:16px;border-radius:50%;background:var(--teal-deep)}
.cover__photo{position:absolute;top:160px;left:0;right:0;height:560px}
.cover__swoosh{position:absolute;left:0;top:560px;width:380px;height:484px}
.cover__headline{position:absolute;left:0;right:0;top:800px;text-align:center;color:#fff;
  font:600 36px "Montserrat",sans-serif;line-height:1.2;letter-spacing:1px}

/* inside panel 1 */
.benefits__photo{height:270px}
.bar{background:var(--lime);color:#fff;font:700 17px "Montserrat",sans-serif;padding:8px 24px;margin:-18px 40px 0 0;position:relative;border-radius:0 18px 18px 0}
.checklist{list-style:none;padding:14px 26px 4px}
.checklist li{display:flex;align-items:center;gap:9px;font-size:14px;margin-bottom:7px}
.checklist .tick{flex:none;width:18px;height:18px;border-radius:50%;background:var(--teal);display:flex;align-items:center;justify-content:center}
.benefits__sub{font:800 15px "Montserrat",sans-serif;color:var(--teal-deep);padding:10px 26px 4px;text-transform:uppercase}
.benefits__text{padding:0 26px}
.bullets{list-style:none;padding:8px 26px}
.bullets li{font-size:13px;margin-bottom:4px;padding-left:16px;position:relative}
.bullets li::before{content:"";position:absolute;left:0;top:6px;width:8px;height:8px;border-radius:50%;background:var(--lime)}

/* inside panel 2 */
.middle__badge{width:56px;height:56px;border-radius:50%;background:#fff;margin:30px auto 14px;border:3px solid var(--lime)}
.middle__title{text-align:center;font:700 21px "Montserrat",sans-serif;margin-bottom:14px}
.middle__body{padding:0 30px}
.middle__body p{margin-bottom:10px;color:#fff}
.truth{font:700 16px "Montserrat",sans-serif;color:#f7e95b;line-height:1.3;margin:4px 0 12px}
.circles{display:flex;justify-content:center;gap:14px;margin:10px 0 16px}
.circles .photo{width:78px;height:78px;border-radius:50%;border:3px solid #fff}
.circles .photo.big{width:96px;height:96px;margin-top:-10px}
.middle__cta{text-align:center;margin-top:8px}
.middle__web{text-align:center;font:600 16px "Montserrat",sans-serif;margin-top:10px}

/* inside panel 3 */
.boost__produce{position:absolute;top:0;right:0;width:170px;height:120px;border-radius:0 0 0 120px}
.boost__title{position:absolute;top:40px;left:26px;width:220px;background:var(--lime);color:#fff;
  font:800 15px "Montserrat",sans-serif;line-height:1.25;padding:10px 14px;border-radius:0 0 18px 0}
.boost__how{position:absolute;top:132px;left:26px;background:var(--teal);color:#fff;font:700 13px "Montserrat",sans-serif;padding:5px 16px;border-radius:14px}
.steps{position:absolute;top:176px;left:26px;right:26px}
.step{margin-bottom:10px}
.step h4{font-size:14px;font-weight:800;color:var(--teal-deep)}
.step h5{font:700 12.5px "Open Sans",sans-serif;color:var(--lime-dark)}
.step p{font-size:12.5px;line-height:1.45}
.other h4{color:var(--lime-dark)}
.boost__photo{position:absolute;left:0;right:0;bottom:0;height:250px;border-radius:160px 0 0 0}
</style>
</head>
<body>

<!-- OUTSIDE -->
<section class="spread spread--outside">
  <article class="panel flap">
    <div class="flap__head">Peptide Weight Loss</div>
    <div class="flap__body">
      <p>Halcrest MD's approach is different: a three step plan using the peptides Veltrazine and KRX5120, stacked with Corvina Balance to heal the gut biome and brain hormone response to weight loss.</p>
      <p>We compound our peptides, so they cost a fraction of the commercial Lunaxor and Trelima, which each run about $1,200 per month.</p>
      <p>Patients are losing as much weight as if they had bariatric surgery: 3–5 pounds per week.</p>
      <p class="flap__callout">If you are like 85% of dieters, it's not your first time. Join thousands pushing past plateaus via Halcrest MD's 16-Week program.</p>
    </div>
    <div class="flap__cta"><span class="phone-pill"><svg viewBox="0 0 24 24" fill="#fff"><path d="M6.6 10.8a15.1 15.1 0 006.6 6.6l2.2-2.2a1 1 0 011-.25 11.4 11.4 0 003.6.57 1 1 0 011 1V20a1 1 0 01-1 1A17 17 0 013 4a1 1 0 011-1h3.5a1 1 0 011 1c0 1.25.2 2.45.57 3.57a1 1 0 01-.25 1z"/></svg>555-318-SLIM</span></div>
    <div class="flap__photo photo" role="img" aria-label="Bathroom scale with a measuring tape on the floor"></div>
    <div class="web-band">www.halcrestmd.com</div>
  </article>

  <article class="panel back teal-bg">
    <div class="back__photo photo" role="img" aria-label="Slim waist in oversized jeans"></div>
    <div class="back__badge"></div>
    <div class="back__body">
      <div class="stars" aria-label="Five star reviews">★★★★★</div>
      <p class="review">"I've been on Veltrazine for one month and dropped 16lbs. Vel will limit your appetite." <b>— Maren</b></p>
      <p class="review">"I've lost 13.5 pounds in a month. I don't want sweets anymore." <b>— Tilda84</b></p>
      <p class="review">"Double peptide plan for a month, down 20 pounds without exercising." <b>— Quinby</b></p>
      <p class="review">"Veltrazine worked for me. 10 out of 10." <b>— Ned</b></p>
      <h2 class="back__drug">VELTRAZINE</h2>
      <p class="back__hunger">HUNGER PANGS!<br>The primary roadblock to weight loss. With veltrazine, hunger pangs are a thing of the past. Veltrazine… changing the game!</p>
    </div>
    <div class="back__cta"><span class="phone-pill"><svg viewBox="0 0 24 24" fill="#fff"><path d="M6.6 10.8a15.1 15.1 0 006.6 6.6l2.2-2.2a1 1 0 011-.25 11.4 11.4 0 003.6.57 1 1 0 011 1V20a1 1 0 01-1 1A17 17 0 013 4a1 1 0 011-1h3.5a1 1 0 011 1c0 1.25.2 2.45.57 3.57a1 1 0 01-.25 1z"/></svg>555-318-SLIM</span></div>
  </article>

  <article class="panel cover">
    <div class="cover__brand">
      <div class="brand-name"><span class="brand-dot"></span>Halcrest MD</div>
    </div>
    <div class="cover__photo photo" role="img" aria-label="Smiling woman measuring her waist with a tape"></div>
    <svg class="cover__swoosh" viewBox="0 0 380 484" preserveAspectRatio="none" aria-hidden="true">
      <path d="M0 110 Q190 10 380 60 L380 484 L0 484Z" fill="#ffffff"/>
      <path d="M0 130 Q190 40 380 80 L380 484 L0 484Z" fill="var(--lime)"/>
      <path d="M0 110 Q190 10 380 60" fill="none" stroke="var(--lime)" stroke-width="4"/>
    </svg>
    <h1 class="cover__headline">LOSE WEIGHT<br>AND KEEP IT OFF</h1>
    <div class="web-band">www.halcrestmd.com</div>
  </article>
</section>

<!-- INSIDE -->
<section class="spread spread--inside">
  <article class="panel benefits">
    <div class="benefits__photo photo" role="img" aria-label="Couple cooking a healthy meal together in a kitchen"></div>
    <h3 class="bar">Benefits of Veltrazine</h3>
    <ul class="checklist">
      <li><span class="tick"><svg width="10" height="10" viewBox="0 0 10 10"><path d="M1.5 5.2l2.2 2.2 4.8-4.8" stroke="#fff" stroke-width="1.8" fill="none"/></svg></span>Reduces hunger pangs</li>
      <li><span class="tick"><svg width="10" height="10" viewBox="0 0 10 10"><path d="M1.5 5.2l2.2 2.2 4.8-4.8" stroke="#fff" stroke-width="1.8" fill="none"/></svg></span>Makes you feel fuller longer</li>
      <li><span class="tick"><svg width="10" height="10" viewBox="0 0 10 10"><path d="M1.5 5.2l2.2 2.2 4.8-4.8" stroke="#fff" stroke-width="1.8" fill="none"/></svg></span>Reduces food cravings</li>
      <li><span class="tick"><svg width="10" height="10" viewBox="0 0 10 10"><path d="M1.5 5.2l2.2 2.2 4.8-4.8" stroke="#fff" stroke-width="1.8" fill="none"/></svg></span>Reduces cardiovascular risk factors</li>
      <li><span class="tick"><svg width="10" height="10" viewBox="0 0 10 10"><path d="M1.5 5.2l2.2 2.2 4.8-4.8" stroke="#fff" stroke-width="1.8" fill="none"/></svg></span>Improves insulin sensitivity</li>
      <li><span class="tick"><svg width="10" height="10" viewBox="0 0 10 10"><path d="M1.5 5.2l2.2 2.2 4.8-4.8" stroke="#fff" stroke-width="1.8" fill="none"/></svg></span>Convenient once-weekly dosing</li>
    </ul>
    <h4 class="benefits__sub">Is Veltrazine safe?</h4>
    <p class="benefits__text">Veltrazine is a safe, FDA-approved medication with minimal side effects.</p>
    <h4 class="benefits__sub">Benefits of KRX 5120</h4>
    <p class="benefits__text">Fat doesn't stand a chance against this naturally powerful peptide, whose fat-fighting abilities provide benefits such as:</p>
    <ul class="bullets">
      <li>Reduces body fat</li>
      <li>Increases calorie burn</li>
      <li>Triggers fat release</li>
      <li>Boosts your metabolism</li>
      <li>Prevents non-fatty foods from turning into body fat</li>
      <li>Doesn't increase your appetite</li>
    </ul>
  </article>

  <article class="panel middle teal-bg">
    <div class="middle__badge"></div>
    <h2 class="middle__title">A weight loss breakthrough</h2>
    <div class="middle__body">
      <p>Recent scientific discoveries offer insight into how our metabolism and hormones change over time — and how that impacts whether we gain or lose weight. It comes down to the relationship between our brains and our guts.</p>
      <p>A new family of medications called GLP-1s address these biological factors head-on.</p>
      <p class="truth">THE TRUTH IS… It's not about willpower. It's biology.</p>
      <p>Up to 70% of weight gain is linked to genetics. Other health conditions and medications can make weight loss even more difficult.</p>
      <div class="circles">
        <div class="photo" role="img" aria-label="Doctor consulting a patient"></div>
        <div class="photo big" role="img" aria-label="Person jogging outdoors"></div>
        <div class="photo" role="img" aria-label="Plate of healthy food"></div>
      </div>
      <p>Peptide GLP-1s fight back against the genetic, biological, and environmental factors that prevent weight loss.</p>
      <div class="middle__cta"><span class="phone-pill"><svg viewBox="0 0 24 24" fill="#fff"><path d="M6.6 10.8a15.1 15.1 0 006.6 6.6l2.2-2.2a1 1 0 011-.25 11.4 11.4 0 003.6.57 1 1 0 011 1V20a1 1 0 01-1 1A17 17 0 013 4a1 1 0 011-1h3.5a1 1 0 011 1c0 1.25.2 2.45.57 3.57a1 1 0 01-.25 1z"/></svg>555-318-SLIM</span></div>
      <div class="middle__web">www.halcrestmd.com</div>
    </div>
  </article>

  <article class="panel boost">
    <div class="boost__produce photo" role="img" aria-label="Fresh fruit and vegetables"></div>
    <h3 class="boost__title">BOOSTING YOUR BODY'S NATURAL ABILITIES</h3>
    <span class="boost__how">How GLP-1s Work</span>
    <div class="steps">
      <div class="step"><h4>WHAT</h4><h5>A naturally occurring hormone</h5><p>GLP-1 is naturally released by the gut in response to food.</p></div>
      <div class="step"><h4>HOW</h4><h5>An extra boost for your system</h5><p>Increases insulin release, slows stomach emptying, and targets brain receptors that reduce appetite.</p></div>
      <div class="step"><h4>RESULT</h4><h5>A more efficient weight loss outcome</h5><p>A sensation of fullness lasting much longer than natural GLP-1 levels allow.</p></div>
      <div class="step other"><h4>Other medications</h4><p>Your Pathwell Clinician may find another medication or combination works best, after a careful review of your case. Call 555-318-SLIM for a free consultation.</p></div>
    </div>
    <div class="boost__photo photo" role="img" aria-label="Woman measuring her waist with a tape"></div>
  </article>
</section>

</body>
</html>
```